Book Cover for Willow Kindred Notes from the Meadow

We have written a book that brings together Notes from the Meadow from a variety of women's voices.
We developed a draft book cover that we like using Canva (attached below). We'd love a book cover that is similar to this image, but looks more professional.
Following are the themes we’d like to depict in the book cover, and in parentheses, how they are represented in the current cover:
1. Divinely feminine (overall cover)
2. Currents of enlightenment (the swirls of light carrying the butterfly)
3. Diversity (a myriad of colors)
4. The solo journey into the unknown (the single butterfly’s flight)
5. Buoyancy and joy (again, the dancing colors and floating butterfly)
6. Boldly feminine (the blue butterfly, set against brush strokes of light)
7. Homage to a dear friend (she loved blue butterflies, the cosmos - this butterfly has hints of the cosmos in her wings, and painting - this background has brush strokes of light).
Book Title, Subtitle, and Editor:
Willow Kindred
Notes from the Meadow
Edited by Mirela Tove
Thank you very much for considering this project!
People who are interested in Women and Spirituality

```html
<!DOCTYPE html>
<html lang="en">
<head>
<meta charset="utf-8">
<title>Willow Kindred — Notes from the Meadow</title>
<link href="https://fonts.googleapis.com/css2?family=Italiana&family=Marcellus&family=Poppins:wght@700&display=swap" rel="stylesheet">
<style>
  :root {
    --sky-top: #e4b48c;
    --sky-mid: #eec7a0;
    --cloud: #5d5552;
    --haze: #93aaa6;
    --mountain: #6d777c;
    --sea: #dcdacd;
    --glow: #efe6c8;
    --rock: #1d1b1a;
    --rock-deep: #131211;
    --ink: #1f1a17;
    --paper: #ffffff;
  }
  html, body {
    margin: 0;
    padding: 0;
    overflow: hidden;
    background: #ffffff;
  }
  .cover {
    position: relative;
    width: 752px;
    height: 1200px;
    overflow: hidden;
  }
  .cover-art {
    position: absolute;
    inset: 0;
    background:
      radial-gradient(ellipse 150px 320px at 420px 760px, rgba(239,230,200,0.55), rgba(239,230,200,0) 70%),
      radial-gradient(ellipse 220px 120px at 120px 960px, rgba(200,196,180,0.45), rgba(200,196,180,0) 70%),
      radial-gradient(ellipse 260px 40px at 300px 80px, rgba(93,85,82,0.45), rgba(93,85,82,0) 70%),
      radial-gradient(ellipse 220px 36px at 600px 120px, rgba(93,85,82,0.4), rgba(93,85,82,0) 70%),
      linear-gradient(180deg,
        var(--sky-top) 0%,
        var(--sky-mid) 18%,
        var(--haze) 27%,
        var(--mountain) 36%,
        #8e979a 44%,
        var(--sea) 50%,
        #c9c5b4 53%,
        #4a4440 58%,
        var(--rock) 68%,
        var(--rock-deep) 100%);
  }
  .series-line {
    position: absolute;
    top: 36px;
    left: 0;
    width: 752px;
    margin: 0;
    text-align: center;
    font-family: "Italiana", serif;
    font-size: 20px;
    line-height: 24px;
    letter-spacing: 7px;
    color: var(--ink);
  }
  .title {
    position: absolute;
    top: 180px;
    left: 0;
    width: 752px;
    margin: 0;
    text-align: center;
    font-family: "Marcellus", serif;
    font-weight: 400;
    font-size: 118px;
    line-height: 110px;
    color: var(--paper);
  }
  .editor {
    position: absolute;
    top: 1064px;
    left: 0;
    width: 752px;
    text-align: center;
    font-family: "Poppins", sans-serif;
    font-weight: 700;
    color: var(--paper);
  }
  .editor-label {
    display: block;
    font-size: 15px;
    line-height: 20px;
  }
  .editor-name {
    display: block;
    margin-top: 2px;
    font-size: 29px;
    line-height: 36px;
    letter-spacing: 0.5px;
  }
</style>
</head>
<body>
  <main class="cover">
    <div class="cover-art" role="img" aria-label="Painted seascape at dusk: peach sky with dark clouds, misty blue mountains, a glowing sea channel running between dark layered rocks, and a lone figure standing on a cliff edge at right"></div>
    <p class="series-line">NOTES FROM THE MEADOW</p>
    <h1 class="title">WILLOW<br>KINDRED</h1>
    <div class="editor">
      <span class="editor-label">EDITED BY</span>
      <span class="editor-name">MIRELA TOVE</span>
    </div>
  </main>
</body>
</html>
```